New Creative Busines Card

Hi Lead Designer,

How are you going?

I was hoping you can help me design the perfect business card for my new business. I have listed below some background information about the business and the concept to help with your design. I'm open to any form of creative ideas, but would like to have two types of colour schemes one dark color and one light.

I would like to have a dark set of design and a light (One design with one in black or dark background and one with light background to compare the contrast since the business card will be double sided one) I imagine this will be pretty easy to change the background of the design. Would prefer one side to have all the details and the other will just have a amazing logo (K7) to give it the finishing touch.

Feel free to email me if you have any questions.

Business Structure and design concepts:

Name of the business: K7 Advisory
Business: Dating agency and event management (Date night etc)
Concept: The main focus will be the K7 ( As some sort of a heart shape like logo) be creative
Details to include in the card will be general details like Name, Title: , Email, mobile, website (Contact details will be given later).

The rest of the idea is up to you, feel free to go crazy with your creative ideas.

Thank you for your help in advance, may the best candidate win~!

Target Market(s)

Target market will be Professional, Elegant, young and ambitious people.

Industry/Entity Type

Business

Requirements
Must have
• Focus on the K7 (as some sort of a heart shape logo). Since this is a double sides design would prefer on one side to focus on the just the K7 logo and the other side with a smaller version of the logo (with it or without) and all the details such as Name, Title, Mobile, Email, Website. Please have the design in landscape format.Not fuss with the Font as long as it is easy to read.
Nice to have
• Different Contrast in colours (keep it simple) one side dark colour scheme and one side light. Prefer to have 3-4 colours (not overwhelm with too many colours) to keep it simple and elegant.
Should not have
• Too colours, main focus is should be the K7 logo not the colours

```html
<!DOCTYPE html>
<html lang="en">
<head>
<meta charset="utf-8">
<title>K7 Advisory – Business Card</title>
<link rel="stylesheet" href="https://fonts.googleapis.com/css2?family=Open+Sans:ital,wght@0,400;0,700;1,700&display=swap">
<style>
  :root {
    --stage: #d6d6d6;
    --stage-edge: #c4c4c4;
    --card: #ffffff;
    --plum-top: #970098;
    --plum-bottom: #62005f;
    --plum: #7a0079;
    --aqua: #16c8d0;
    --ink-light: #ffffff;
  }
  * { margin: 0; padding: 0; box-sizing: border-box; }
  html, body { width: 934px; height: 1200px; overflow: hidden; }
  body {
    position: relative;
    background: radial-gradient(ellipse at center, var(--stage) 60%, var(--stage-edge) 100%);
    font-family: "Open Sans", Arial, sans-serif;
  }
  .card {
    position: absolute;
    left: 33px;
    width: 869px;
    height: 540px;
    background: var(--card);
    overflow: hidden;
  }
  .card--details { top: 59px; }
  .card--brand { top: 599px; }

  .card__panel { position: absolute; left: 0; top: 0; width: 869px; height: 540px; }

  .holder { position: absolute; left: 0; top: 0; color: var(--ink-light); }
  .holder__name {
    position: absolute; left: 94px; top: 122px;
    font-size: 29px; font-weight: 700; font-style: italic; white-space: nowrap;
  }
  .holder__rule {
    position: absolute; left: 56px; top: 165px; width: 405px; height: 2px;
    background: var(--ink-light);
  }
  .holder__title {
    position: absolute; left: 94px; top: 173px;
    font-size: 29px; font-weight: 400; white-space: nowrap;
  }

  .contact { position: absolute; left: 0; top: 0; list-style: none; color: var(--ink-light); }
  .contact__item {
    position: absolute; left: 84px; height: 32px; width: 380px;
    display: flex; align-items: center; font-size: 21px; white-space: nowrap;
  }
  .contact__icon { width: 30px; height: 30px; margin-right: 15px; flex: none; }

  .wordmark {
    position: absolute; display: flex; align-items: center; gap: 16px;
    color: var(--plum); font-weight: 700; white-space: nowrap;
  }
  .wordmark__dot { border-radius: 50%; background: var(--aqua); flex: none; }
  .wordmark--small { left: 535px; top: 300px; font-size: 40px; }
  .wordmark--small .wordmark__dot { width: 30px; height: 30px; }
  .wordmark--large { left: 0; width: 869px; justify-content: center; top: 250px; font-size: 64px; }
  .wordmark--large .wordmark__dot { width: 46px; height: 46px; }
</style>
</head>
<body>

<section class="card card--details" aria-label="Card front with contact details">
  <svg class="card__panel" viewBox="0 0 869 540" aria-hidden="true">
    <defs>
      <linearGradient id="plumFade" x1="0" y1="0" x2="0" y2="1">
        <stop offset="0" stop-color="var(--plum-top)"/>
        <stop offset="1" stop-color="var(--plum-bottom)"/>
      </linearGradient>
    </defs>
    <path d="M0 0 H414 Q526 270 414 540 H0 Z" fill="url(#plumFade)"/>
  </svg>

  <div class="holder">
    <p class="holder__name">Name</p>
    <div class="holder__rule"></div>
    <p class="holder__title">Title</p>
  </div>

  <ul class="contact">
    <li class="contact__item" style="top:268px">
      <svg class="contact__icon" viewBox="0 0 30 30" aria-hidden="true">
        <path d="M11 4 h4 v6 h-3 q-1 5 0 10 h3 v6 h-4 q-5 -11 0 -22 z" fill="#fff"/>
      </svg>
      +(000) 1234 5678
    </li>
    <li class="contact__item" style="top:307px">
      <svg class="contact__icon" viewBox="0 0 30 30" aria-hidden="true" fill="none" stroke="#fff" stroke-width="1.6">
        <rect x="9" y="3" width="12" height="9"/>
        <rect x="3" y="12" width="24" height="9"/>
        <rect x="7" y="21" width="16" height="6"/>
        <line x1="11" y1="6" x2="19" y2="6"/><line x1="11" y1="9" x2="19" y2="9"/>
      </svg>
      name@emailaddress.com
    </li>
    <li class="contact__item" style="top:349px">
      <svg class="contact__icon" viewBox="0 0 30 30" aria-hidden="true">
        <path d="M15 2 a9 9 0 0 1 9 9 c0 7 -9 17 -9 17 s-9 -10 -9 -17 a9 9 0 0 1 9 -9 z" fill="#fff"/>
        <circle cx="15" cy="11" r="4" fill="var(--plum)"/>
      </svg>
      your address, address 1
    </li>
    <li class="contact__item" style="top:392px">
      <svg class="contact__icon" viewBox="0 0 30 30" aria-hidden="true" fill="none" stroke="#fff" stroke-width="1.3">
        <circle cx="15" cy="15" r="12"/>
        <ellipse cx="15" cy="15" rx="5" ry="12"/>
        <line x1="3" y1="15" x2="27" y2="15"/>
        <line x1="15" y1="3" x2="15" y2="27"/>
        <path d="M5 9 h20 M5 21 h20"/>
      </svg>
      www.website.com
    </li>
  </ul>

  <div class="wordmark wordmark--small">
    <span class="wordmark__dot"></span>K7 Advisory
  </div>
</section>

<section class="card card--brand" aria-label="Card back with brand name">
  <div class="wordmark wordmark--large">
    <span class="wordmark__dot"></span>K7 Advisory
  </div>
</section>

</body>
</html>
```